Flyer for Programming Classes for Kids

We are small school in Tokyo, Japan teaching computer programming to kids in English.
We need a flyer to promote our classes and provide basic information about our company.
See Flyer_Notes.doc for more company info, class info, and flyer requirements.
Basic Info:
One page flyer. Two-sided, front and back.
We would like a flyer that introduces the company. -and-
Highlights the classes we offer
Target Market: 6-12 year old kids and their parents. Audience is English speaking families in Japan.
Look And Feel: Bold, Playful, Modern, Conservative
Paper Size: B4
What is B4? https://www.quorvanta.com/products/resources/paper-sizes-and-formats-explained.php
Target Market(s)
Tokyo, but English speakers
Industry/Entity Type
Education
Colors
Designer to choose colors to be used in the design.
Look and feel
Each slider illustrates characteristics of the customer's brand and the style your logo design should communicate.

```html
<!DOCTYPE html>
<html lang="en">
<head>
<meta charset="utf-8">
<title>Pixel Sprout Lab – Class Flyer</title>
<link rel="stylesheet" href="https://fonts.googleapis.com/css2?family=Jost:wght@400;500&family=Cormorant+Garamond:wght@500&display=swap">
<style>
  :root {
    --red: #ea1d24;
    --blue: #2e7fc1;
    --white: #ffffff;
    --ink: #2b2b2b;
    --gold: #a8894f;
    --stage: #e9e9ec;
    --photo-dark: #5a5654;
    --photo-light: #b9b2ad;
  }
  * { box-sizing: border-box; margin: 0; padding: 0; }
  html, body { width: 1041px; height: 1200px; overflow: hidden; background: var(--stage); }
  body { font-family: "Jost", "Century Gothic", sans-serif; }

  .flyer {
    position: absolute; left: 97px; top: 0;
    width: 847px; height: 1200px;
    background: var(--white); overflow: hidden;
    text-transform: uppercase;
  }

  /* award block */
  .award { position: absolute; left: 22px; top: 52px; width: 240px; text-align: center; }
  .award-badge { display: block; width: 150px; height: 150px; margin: 0 auto 12px; border-radius: 50%; background: radial-gradient(circle, #d8c08a 0%, var(--gold) 70%); }
  .award-title { font-family: "Cormorant Garamond", serif; font-size: 21px; color: var(--ink); letter-spacing: .5px; padding-bottom: 3px; border-bottom: 1px solid var(--ink); }
  .award-sub { font-family: "Cormorant Garamond", serif; font-size: 12px; color: var(--ink); line-height: 14px; margin-top: 3px; }
  .brand-name { font-size: 27px; color: var(--gold); font-weight: 400; margin-top: 4px; letter-spacing: .5px; }

  /* photo placeholders */
  .photo { position: absolute; border-radius: 50%; background: linear-gradient(150deg, var(--photo-light), var(--photo-dark)); }
  .photo-hero { left: 506px; top: -8px; width: 356px; height: 356px; border: 7px solid var(--red); }
  .photo-student { left: 648px; top: 594px; width: 206px; height: 206px; border: 6px solid var(--white); z-index: 2; }

  /* class circles */
  .class-row { position: absolute; left: 0; top: 408px; width: 847px; height: 160px; }
  .class-chip {
    position: absolute; top: 0; width: 160px; height: 160px; border-radius: 50%;
    background: var(--red); border: 6px solid var(--white);
    display: flex; align-items: center; justify-content: center; text-align: center;
    color: var(--white); font-size: 19px; line-height: 23px; font-weight: 400;
  }

  /* info bands */
  .band { position: absolute; left: 0; font-size: 14px; line-height: 17.3px; }
  .band-blue { background: var(--blue); color: var(--white); }
  .band-white { color: var(--blue); }
  .band p { white-space: nowrap; }

  .b-beginner { top: 616px; width: 666px; height: 128px; padding: 10px 0 0 18px; }
  .b-intermediate { top: 744px; width: 847px; height: 114px; padding: 11px 0 0 17px; }
  .b-tinker { top: 858px; width: 718px; height: 109px; padding: 9px 0 0 17px; }
  .b-tide { top: 967px; width: 847px; height: 104px; padding: 18px 0 0 17px; }
  .b-about { top: 1071px; width: 847px; height: 129px; padding: 26px 0 0 34px; }

  .icon-braces { position: absolute; left: 731px; top: 868px; width: 106px; height: 90px; }
</style>
</head>
<body>
<main class="flyer">

  <header class="award">
    <span class="award-badge" aria-hidden="true"></span>
    <p class="award-title">School of the Year</p>
    <p class="award-sub">- Computer Science -<br>(Newcomer)</p>
    <p class="brand-name">Pixel Sprout Lab</p>
  </header>

  <div class="photo photo-hero" role="img" aria-label="Photo of children coding on laptops in a classroom"></div>

  <section class="class-row" aria-label="Classes offered">
    <div class="class-chip" style="left:26px">Ages 6-12</div>
    <div class="class-chip" style="left:190px">Beginner<br>Snapblox</div>
    <div class="class-chip" style="left:344px">Intermediate<br>Snapblox</div>
    <div class="class-chip" style="left:496px">Tinker<br>Garage<br>Workshop</div>
    <div class="class-chip" style="left:650px">Tidescript</div>
  </section>

  <div class="photo photo-student" role="img" aria-label="Photo of a student working at a laptop"></div>

  <section class="band band-blue b-beginner">
    <p>&lt;Class Info</p>
    <p style="padding-left:17px">&lt; Beginner Snapblox</p>
    <p style="padding-left:34px">&lt; For kids new to coding.&nbsp; Learn to program using Snapblox, a fun</p>
    <p>and easy to use language. Make games, interactive stories, animations,</p>
    <p>and more, all while learning the fundamentals of computer programming.</p>
    <p style="padding-left:34px">&lt; For students with little or no experience.</p>
  </section>

  <section class="band band-white b-intermediate">
    <p style="padding-left:45px">Intermediate Snapblox</p>
    <p style="padding-left:50px">&lt; Kids learn more advanced programming concepts in Snapblox and</p>
    <p>create larger and more complex programs. They plan, design,</p>
    <p>and create their own coding projects, from start to finish.</p>
    <p style="padding-left:55px">&lt; For students who have completed Beginner Snapblox 1 &amp; 2 or have prior</p>
    <p>coding experience.</p>
  </section>

  <section class="band band-blue b-tinker">
    <p style="padding-left:32px">&lt; Tinker Garage Workshop</p>
    <p style="padding-left:50px">&lt; Continue to learn and explore coding&nbsp; in a collaborative, fun space.</p>
    <p>Each lesson kids complete a new, STEM based coding project.</p>
    <p style="padding-left:4px">Projects cover physics, math, story telling, game design, Brick robotics, and more.</p>
    <p style="padding-left:50px">&lt; Recommended for intermediate students.</p>
  </section>

  <svg class="icon-braces" viewBox="0 0 106 90" role="img" aria-label="Code braces icon">
    <g fill="none" stroke="var(--ink)" stroke-width="9" stroke-linecap="round" stroke-linejoin="round">
      <path d="M30 7 C19 7 17 12 17 22 L17 34 C17 41 13 45 7 45 C13 45 17 49 17 56 L17 68 C17 78 19 83 30 83"/>
      <path d="M76 7 C87 7 89 12 89 22 L89 34 C89 41 93 45 99 45 C93 45 89 49 89 56 L89 68 C89 78 87 83 76 83"/>
    </g>
    <circle cx="53" cy="32" r="7.5" fill="var(--ink)"/>
    <circle cx="53" cy="59" r="7.5" fill="var(--ink)"/>
  </svg>

  <section class="band band-white b-tide">
    <p style="padding-left:34px">&lt; Tidescript</p>
    <p style="padding-left:50px">&lt; Learn to code in one of the most popular text based languages. Tidescript 101 teaches kids</p>
    <p>the basics of Tidescript coding with an emphasis on mathematics and computer science fundamentals.</p>
    <p style="padding-left:50px">&lt; For students aged 12-17 with little or no experience.</p>
  </section>

  <section class="band band-blue b-about">
    <p>&lt; Our curriculum is based on&nbsp; STEM (Science, Technology, Engineering, and Math) with</p>
    <p style="padding-left:14px">a pinch of art, and whole lot of creativity. Kids learn core, computer science fundamentals</p>
    <p style="padding-left:14px">while solving STEM based projects and tapping into their creative minds.</p>
  </section>

</main>
</body>
</html>
```